Modernes Briefpapier für Steuerberater
Zielgruppe
Ich bin Steuerbertaer und brauche ein modernes Briefpapier, was elegant, aber seriös daherkommt.
Aufgabenstellung
Ein Briefpapier mit meinem Logo. Gerne in die Richtung des anderen angehängten Bildes vom Design her.

```html
<!DOCTYPE html>
<html lang="de">
<head>
<meta charset="utf-8">
<title>Kellermann Steuerberatung – Geschäftsausstattung</title>
<link rel="stylesheet" href="https://fonts.googleapis.com/css2?family=Source+Sans+3:wght@400;600;700&display=swap">
<style>
:root{
  --blue:#2aa8e2;
  --ink:#3a3a3a;
  --grey:#6d6e71;
  --paper:#ffffff;
  --stage:#e9edf2;
  --fold:#e6e7e9;
}
*{margin:0;padding:0;box-sizing:border-box}
html,body{width:1200px;height:869px;overflow:hidden;background:var(--stage);font-family:"Source Sans 3",sans-serif;color:var(--ink)}
.sheet{position:absolute;background:var(--paper);box-shadow:0 2px 6px rgba(0,0,0,.18);overflow:hidden}
.brand{position:absolute;display:flex;align-items:center;gap:6px;font-weight:600;color:var(--grey);white-space:nowrap;letter-spacing:.02em}
.brand .mark{border:1.5px solid var(--blue);display:inline-block}
.band{position:absolute;left:0;bottom:0;width:100%}
.small{position:absolute;font-size:6px;line-height:8px;white-space:nowrap}
.blue{color:var(--blue);font-weight:600}
.bold{font-weight:700}
/* letterhead */
.letter{left:115px;top:116px;width:447px;height:625px}
.letter .head{position:absolute;left:0;top:0;width:100%;height:208px;background:linear-gradient(#fff 45%,#e4e5e7)}
.letter .brand{left:43px;top:42px;font-size:10.5px}
.letter .brand .mark{width:29px;height:29px}
.sender-line{position:absolute;left:43px;top:109px;font-size:5.6px;border-bottom:.6px solid var(--ink);white-space:nowrap}
.recipient{position:absolute;left:43px;top:139px;font-size:7.4px;line-height:10px;color:var(--grey)}
.contact{left:311px;top:88px;line-height:8.6px}
.ico{display:inline-block;width:5px;height:5px;background:var(--blue);border-radius:1px;margin-right:3px;vertical-align:middle}
.fold{position:absolute;left:0;width:9px;height:.7px;background:#888}
.body{position:absolute;left:43px;top:228px;width:362px;font-size:7.4px;line-height:10px;text-align:justify;color:var(--ink)}
.body p{margin-bottom:10px}
.foot{top:582px}
.badge{position:absolute;border-radius:3px}
/* cards */
.card{top:120px;width:178px;height:115px}
.card1{left:621px}
.card2{left:822px}
.card1 .brand{left:30px;top:48px;font-size:7px}
.card1 .brand .mark{width:17px;height:17px}
.card2 .brand{left:86px;top:19px;font-size:4.4px}
.card2 .brand .mark{width:12px;height:12px}
.portrait{position:absolute;left:13px;top:18px;width:45px;height:45px;background:linear-gradient(#5a6068,#2d3137)}
.card2 .small{left:86px;font-size:4.6px;line-height:6.2px}
/* envelopes */
.env-back{left:618px;top:261px;width:460px;height:229px}
.flap{position:absolute;left:6px;top:0;width:448px;height:64px;border:1px solid var(--fold);border-top:none;border-radius:0 0 30px 30px}
.env-back .return{position:absolute;left:0;width:100%;top:209px;text-align:center;font-size:8px;color:var(--grey)}
.env-front{left:619px;top:512px;width:458px;height:233px}
.env-front .brand{left:37px;top:53px;font-size:7.6px}
.env-front .brand .mark{width:20px;height:20px}
.window{position:absolute;left:41px;top:104px;width:188px;height:93px;border:2px solid var(--fold);border-radius:14px;background:linear-gradient(#fafafa,#f0f0f0)}
</style>
</head>
<body>

<!-- Letterhead -->
<section class="sheet letter">
  <div class="head"></div>
  <div class="brand"><span class="mark"></span>KELLERMANN | STEUERBERATUNG</div>
  <div class="sender-line"><b>Kellermann I Steuerberatung</b> | Lindenweg 12 | 35390 Talheim</div>
  <div class="fold" style="top:146px"></div>
  <div class="fold" style="top:374px"></div>
  <address class="recipient" style="font-style:normal">Markus Manuss<br>Firma Markussd<br>Anussstrasse 23<br>89765 Manusde</address>
  <div class="small contact">
    <span class="blue">Jonas Kellermann</span><br>
    Dipl.-Betriebswirt (FH), Steuerberater<br>
    <span style="display:block;height:5px"></span>
    Lindenweg 12 | 35390 Talheim<br>
    <span class="ico"></span>0641 - 555 124 00<br>
    <span class="ico"></span>0170 - 5558821<br>
    <span class="ico"></span>info@kellermann-steuer.de<br>
    <span class="ico"></span>www.kellermann-steuer.de<br>
    <span style="display:block;height:6px"></span>
    Talheim, 01. August 2018<br>
    <span style="display:block;height:6px"></span>
    <span class="bold">Ihre Kundendaten</span><br>
    Kundennummer: 431 15754
  </div>
  <div class="body">
    <p>Lorem ipsum dolor sit</p>
    <p>Lorem ipsum dolor sit amet, consectetuer adipiscing elit. Aenean commodo ligula eget dolor. Aenean massa. Cum sociis natoque penatibus et magnis dis parturient montes, nascetur ridiculus mus. Donec quam felis, ultricies nec, pellentesque eu, pretium quis, sem. Nulla consequat massa quis enim. Donec pede justo, fringilla vel, aliquet nec, vulputate eget, arcu. In enim justo, rhoncus ut, imperdiet a, venenatis vitae, justo. Nullam dictum felis eu pede mollis pretium. Integer tincidunt. Cras dapibus. Vivamus elementum semper</p>
    <p>nisi. Aenean vulputate eleifend tellus. Aenean leo ligula, porttitor eu, consequat vitae, eleifend ac, enim. Aliquam lorem ante, dapibus in, viverra quis, feugiat a, tellus. Phasellus viverra nulla ut metus varius laoreet. Quisque rutrum. Aenean imperdiet. Etiam ultricies nisi vel augue. Curabitur ullamcorper ultricies nisi. Nam eget dui. Etiam rhoncus. Maecenas tempus, tellus eget condimentum rhoncus, sem quam semper libero, sit</p>
    <p>nisi. Aenean vulputate eleifend tellus. Aenean leo ligula, porttitor eu, consequat vitae, eleifend ac, enim. Aliquam lorem ante, dapibus in, viverra quis, feugiat a, tellus. Phasellus viverra nulla ut metus varius laoreet. Quisque rutrum. Aenean imperdiet. Etiam ultricies nisi vel augue. Curabitur ullamcorper ultricies nisi. Nam</p>
  </div>
  <div class="small foot" style="left:43px"><span class="bold">Jonas Kellermann</span><br>Dipl.-Betriebswirt (FH), Steuerberater<br>USt-ID: DE 000111222</div>
  <div class="small foot" style="left:177px">Kreisbank Talheim<br>IBAN: DE 00 1234 0000 0012 3456 78<br>BIC: KRTADE5TXXX</div>
  <div class="badge" style="left:280px;top:584px;width:56px;height:26px;background:#d8d9db"></div>
  <div class="badge" style="left:355px;top:570px;width:50px;height:40px;background:#d8d9db"></div>
  <svg class="band" width="447" height="12" viewBox="0 0 447 12"><path d="M0 1H320L330 12H0Z" fill="var(--blue)"/><rect x="0" y="9" width="447" height="3" fill="var(--blue)"/></svg>
</section>

<!-- Business card front -->
<section class="sheet card card1">
  <div class="brand"><span class="mark"></span>KELLERMANN | STEUERBERATUNG</div>
  <svg class="band" width="178" height="8" viewBox="0 0 178 8"><path d="M0 0H95L102 8H0Z" fill="var(--blue)"/><rect x="0" y="6" width="178" height="2" fill="var(--blue)"/></svg>
</section>

<!-- Business card back -->
<section class="sheet card card2">
  <div class="portrait" role="img" aria-label="Porträtfoto des Steuerberaters"></div>
  <div class="brand"><span class="mark"></span>KELLERMANN | STEUERBERATUNG</div>
  <div class="small" style="top:47px"><span class="blue">Jonas Kellermann</span><br>Dipl.-Betriebswirt (FH), Steuerberater</div>
  <div class="small" style="top:62px">Lindenweg 12 | 35390 Talheim</div>
  <div class="small" style="top:73px"><span class="ico" style="width:3px;height:3px"></span>0641 - 555 124 00<br><span class="ico" style="width:3px;height:3px"></span>0170 - 5558821</div>
  <div class="small" style="top:89px"><span class="ico" style="width:3px;height:3px"></span>info@kellermann-steuer.de<br><span class="ico" style="width:3px;height:3px"></span>www.kellermann-steuer.de</div>
  <svg class="band" width="178" height="8" viewBox="0 0 178 8"><path d="M0 0H95L102 8H0Z" fill="var(--blue)"/><rect x="0" y="6" width="178" height="2" fill="var(--blue)"/></svg>
</section>

<!-- Envelope back -->
<section class="sheet env-back">
  <div class="flap"></div>
  <div class="return">Kellermann I Steuerberatung | Lindenweg 12 | 35390 Talheim</div>
</section>

<!-- Envelope front -->
<section class="sheet env-front">
  <div class="brand"><span class="mark"></span>KELLERMANN | STEUERBERATUNG</div>
  <div class="window"></div>
  <svg class="band" width="458" height="9" viewBox="0 0 458 9"><path d="M0 0H110L118 9H0Z" fill="var(--blue)"/><rect x="0" y="6" width="458" height="3" fill="var(--blue)"/></svg>
</section>

</body>
</html>
```